Branding label contest for 2 great products

I require labels for our health food treat dry packs and coffee business. The packaging at this stage consists of the follow... plastic food pouches for dry ingredients and takeaway coffee cups. The coffee cup artwork/design will be for standard small, medium and large paper takeaway coffee cups and the food pouch size 190mmW x 260mmL. the pouch design will need to be customisable to allow use across a range of products. for reference please visit www.torvimelu.com.au and instagram @torvimelu for products. I have attached our logo and business card files for your perusal.

Target Market(s)

Healthy conscious, vegan, paleo, gluten free, all round fitness fanatics and yogis

Industry/Entity Type

Business

Requirements
Must have
• Earthy tones, our logo. Rustic earthy feel. trendy artwork.
Should not have
• Bright colours

```html
<!DOCTYPE html>
<html lang="en">
<head>
<meta charset="utf-8">
<title>Torvi Melu – Cookie Time Label</title>
<link rel="stylesheet" href="https://fonts.googleapis.com/css2?family=Cabin:wght@400;500;600&display=swap">
<style>
  :root {
    --stage: #f3f0ee;
    --damask: #e6e1e3;
    --frame: #7d6470;
    --kraft: #a4877e;
    --kraft-dark: #957870;
    --cup-shadow: rgba(110, 80, 78, 0.35);
    --band: #ede6e2;
    --ink: #6b5460;
    --ink-soft: #6f5a63;
    --plate: #f4f2f3;
    --plate-ring: #7d6470;
    --footer: #7f6570;
    --footer-text: #ffffff;
    --logo-text: #c9a096;
    --cookie-light: #e7cf8a;
    --cookie-mid: #c99a5c;
    --cookie-dark: #8d6a55;
  }
  * { box-sizing: border-box; margin: 0; padding: 0; }
  html, body {
    width: 1200px; height: 730px; overflow: hidden;
    background: var(--stage);
    font-family: "Cabin", "Helvetica Neue", Arial, sans-serif;
  }
  .canvas { position: relative; width: 1200px; height: 730px; }

  .label {
    position: absolute; left: 332px; top: 0;
    width: 536px; height: 730px;
  }
  .label__pattern {
    position: absolute; inset: 0;
    background: var(--damask);
  }
  .label__panel {
    position: absolute; left: 28px; top: 30px;
    width: 482px; height: 668px;
    border: 7px solid var(--frame);
    background: linear-gradient(160deg, var(--kraft), var(--kraft-dark));
    overflow: hidden;
  }
  .label__cup-art {
    position: absolute; left: 14px; top: 300px;
    width: 440px; height: 280px;
    background: var(--cup-shadow);
    border-radius: 0 0 120px 120px;
    opacity: 0.55;
  }

  .brand-seal {
    position: absolute; left: 175px; top: 41px;
    width: 172px; height: 172px; border-radius: 50%;
    background: #ffffff;
    display: flex; align-items: center; justify-content: center;
  }
  .brand-seal__name {
    font-weight: 500; font-size: 25px; letter-spacing: 3px;
    color: var(--logo-text); text-transform: uppercase;
    text-align: center; line-height: 1.2;
  }

  .headline-band {
    position: absolute; left: 1px; top: 193px;
    width: 466px; height: 108px;
    background: var(--band);
    text-align: center;
  }
  .headline-band__title {
    padding-top: 14px;
    font-weight: 600; font-size: 54px; line-height: 1;
    color: var(--ink); letter-spacing: -0.5px;
  }
  .headline-band__subtitle {
    margin-top: 6px;
    font-weight: 400; font-size: 24px; line-height: 1;
    color: var(--ink-soft);
  }

  .plate {
    position: absolute; left: 99px; top: 312px;
    width: 276px; height: 276px;
  }

  .footer {
    position: absolute; left: 0; bottom: 0;
    width: 468px; height: 58px;
    background: var(--footer);
    color: var(--footer-text);
    display: flex; justify-content: space-between; align-items: center;
    padding: 0 18px;
  }
  .footer__contact { font-size: 14px; font-weight: 500; line-height: 1.35; }
  .footer__social { font-size: 14px; font-weight: 500; display: flex; align-items: center; gap: 6px; }
</style>
</head>
<body>
<main class="canvas">
  <section class="label">
    <div class="label__pattern" role="img" aria-label="Soft grey damask pattern border"></div>
    <div class="label__panel">
      <div class="label__cup-art" role="img" aria-label="Faint illustration of a steaming coffee cup on a saucer"></div>

      <div class="brand-seal">
        <span class="brand-seal__name">Torvi<br>Melu</span>
      </div>

      <div class="headline-band">
        <h1 class="headline-band__title">ITS COOKIE TIME</h1>
        <p class="headline-band__subtitle">NEED A COFFEE BREAK</p>
      </div>

      <svg class="plate" viewBox="0 0 276 276" aria-hidden="false">
        <defs>
          <radialGradient id="cookie-tones" cx="50%" cy="45%" r="55%">
            <stop offset="0%" stop-color="var(--cookie-light)"/>
            <stop offset="60%" stop-color="var(--cookie-mid)"/>
            <stop offset="100%" stop-color="var(--cookie-dark)"/>
          </radialGradient>
        </defs>
        <circle cx="138" cy="138" r="136" fill="var(--plate)"/>
        <circle cx="138" cy="138" r="126" fill="none" stroke="var(--plate-ring)" stroke-width="4"/>
        <circle cx="138" cy="138" r="118" fill="none" stroke="var(--plate-ring)" stroke-width="2"/>
        <circle cx="138" cy="138" r="96" fill="none" stroke="#e4e0e2" stroke-width="1"/>
        <ellipse cx="138" cy="140" rx="92" ry="90" fill="url(#cookie-tones)" role="img" aria-label="Photo of three oat and coconut cookies on the plate"/>
      </svg>

      <footer class="footer">
        <div class="footer__contact">
          <div>0412365870</div>
          <div>www.torvimelu.com.au</div>
        </div>
        <div class="footer__social">Follow us <span>@torvimelu</span></div>
      </footer>
    </div>
  </section>
</main>
</body>
</html>
```